Kestrel Path Business card

We are a company that owns 2 compliance software programs for TV, Radio and Cable industries as well as an online job board. We need a professional business card that incorproates all three logos.

```html
<!DOCTYPE html>
<html lang="en">
<head>
<meta charset="utf-8">
<title>Kestrel Path Business Card</title>
<link rel="stylesheet" href="https://fonts.googleapis.com/css2?family=Roboto+Condensed:wght@400;700&display=swap">
<style>
  :root {
    --navy: #2b2a78;
    --red: #e0402b;
    --white: #ffffff;
    --faint: #c9ccd6;
    --faint-warm: #f2c9b8;
    --watermark: #e6e7ee;
    --bg: #8a8b8d;
  }
  * { margin: 0; padding: 0; box-sizing: border-box; }
  html, body { width: 1200px; height: 1200px; overflow: hidden; }
  body {
    background: var(--bg);
    font-family: "Roboto Condensed", sans-serif;
    color: var(--navy);
    position: relative;
  }
  .card {
    position: absolute;
    left: 190px;
    width: 820px;
    height: 480px;
    box-shadow: 0 10px 30px rgba(0,0,0,0.25);
  }
  .card--front { top: 90px; }
  .card--back { top: 630px; }
  .card__border {
    position: absolute; inset: 0;
    background: linear-gradient(135deg, var(--navy) 0%, var(--navy) 70%, #5a3266 100%);
  }
  .card__panel {
    position: absolute; inset: 28px;
    background: var(--white);
    border-radius: 12px;
  }

  .name-block { position: absolute; top: 70px; left: 0; right: 0; text-align: center; }
  .name-block__name { font-size: 44px; font-weight: 700; letter-spacing: 0.5px; }
  .name-block__role { font-size: 22px; margin-top: 2px; }

  .logo-row {
    position: absolute; top: 215px; left: 0; right: 0;
    display: flex; justify-content: center; align-items: center; gap: 28px;
  }
  .logo-row__sep { width: 2px; height: 40px; background: var(--faint); }

  .brand { display: inline-flex; align-items: center; gap: 8px; font-weight: 700; white-space: nowrap; }
  .brand__dot { width: 14px; height: 14px; border-radius: 50%; flex: none; }
  .brand--muted { color: #a9acc0; font-size: 30px; }
  .brand--muted .brand__dot { background: var(--faint-warm); }
  .brand--primary { color: var(--navy); font-size: 30px; }
  .brand--primary .brand__dot { background: var(--red); }

  .web { position: absolute; right: 70px; bottom: 50px; font-size: 22px; font-weight: 700; }

  .back__logo-a { position: absolute; top: 40px; left: 50px; }
  .back__logo-b { position: absolute; top: 40px; right: 50px; }
  .back__logo-c { position: absolute; bottom: 50px; right: 50px; }

  .watermark {
    position: absolute; top: 120px; left: 320px;
    display: flex; flex-direction: column; gap: 8px;
    color: var(--watermark); font-weight: 700; font-size: 34px;
    line-height: 1.1;
  }

  .address { position: absolute; left: 50px; top: 140px; display: flex; gap: 12px; align-items: flex-start; }
  .address__text { font-size: 24px; line-height: 1.2; }

  .contacts { position: absolute; left: 50px; bottom: 40px; display: flex; flex-direction: column; gap: 10px; }
  .contact { display: flex; align-items: center; gap: 12px; font-size: 22px; }
  .icon { width: 30px; height: 30px; flex: none; }
</style>
</head>
<body>

<section class="card card--front" aria-label="Business card front">
  <div class="card__border" role="img" aria-label="Navy and red angled border pattern"></div>
  <div class="card__panel">
    <div class="name-block">
      <div class="name-block__name">Your Name Here</div>
      <div class="name-block__role">Designation</div>
    </div>
    <div class="logo-row">
      <span class="brand brand--muted"><span class="brand__dot"></span>Airwave Ledger</span>
      <span class="logo-row__sep"></span>
      <span class="brand brand--muted"><span class="brand__dot"></span>Cableline Check</span>
      <span class="logo-row__sep"></span>
      <span class="brand brand--muted"><span class="brand__dot"></span>StageRoster</span>
    </div>
    <div class="web">www.yourweb.com</div>
  </div>
</section>

<section class="card card--back" aria-label="Business card back">
  <div class="card__border" role="img" aria-label="Navy and red angled border pattern"></div>
  <div class="card__panel">
    <div class="watermark" aria-hidden="true">
      <span>Airwave Ledger</span>
      <span>Cableline Check</span>
      <span>StageRoster</span>
    </div>
    <span class="brand brand--primary back__logo-a"><span class="brand__dot"></span>Airwave Ledger</span>
    <span class="brand brand--primary back__logo-b"><span class="brand__dot"></span>StageRoster</span>
    <span class="brand brand--primary back__logo-c"><span class="brand__dot"></span>Cableline Check</span>

    <div class="address">
      <svg class="icon" viewBox="0 0 30 30" aria-hidden="true">
        <path d="M15 3a8 8 0 0 0-8 8c0 6 8 16 8 16s8-10 8-16a8 8 0 0 0-8-8z" fill="none" stroke="var(--red)" stroke-width="2.5"/>
        <circle cx="15" cy="11" r="3" fill="var(--red)"/>
      </svg>
      <div class="address__text">Your Address here<br>NY, United States</div>
    </div>

    <div class="contacts">
      <div class="contact">
        <svg class="icon" viewBox="0 0 30 30" aria-hidden="true">
          <circle cx="15" cy="15" r="15" fill="var(--red)"/>
          <path d="M10 8l3 3-2 2a10 10 0 0 0 6 6l2-2 3 3-2 3c-7 0-13-6-13-13z" fill="var(--white)"/>
        </svg>
        <span>+1 555 010 2525</span>
      </div>
      <div class="contact">
        <svg class="icon" viewBox="0 0 30 30" aria-hidden="true">
          <circle cx="15" cy="15" r="15" fill="var(--red)"/>
          <rect x="8" y="10" width="14" height="10" fill="none" stroke="var(--white)" stroke-width="2"/>
          <path d="M8 10l7 6 7-6" fill="none" stroke="var(--white)" stroke-width="2"/>
        </svg>
        <span>yourmail@mail.com</span>
      </div>
      <div class="contact">
        <svg class="icon" viewBox="0 0 30 30" aria-hidden="true">
          <circle cx="15" cy="15" r="15" fill="var(--red)"/>
          <circle cx="15" cy="15" r="8" fill="none" stroke="var(--white)" stroke-width="2"/>
          <ellipse cx="15" cy="15" rx="3.5" ry="8" fill="none" stroke="var(--white)" stroke-width="1.5"/>
          <path d="M7 15h16" stroke="var(--white)" stroke-width="1.5"/>
        </svg>
        <span>www.yourweb.com</span>
      </div>
    </div>
  </div>
</section>

</body>
</html>
```